Autobody repair paint repairs spray painting bodywork crash repairs

Details for my new Facebook Design Project will be added sooAUTOMOTIVE REPAIR. CAR / MOTORCYCLES GOT LOGO DESIGN / DID THINK ABOUT FACEBOOK DONT NOALREADY HAVE WEB ADRESS www.brightpanel.co.uk and mail sales@brightpanel,co.uk NEED SOMETHINK I CAN MANAGE TO UPLOAD PICTURES IN TO A GALLERY OR SOMETHINGLIKE THAT I ALSO SELL CAR AND MOTORCYCLES MAYBE A SELLS PAGE WITH A COINDROP LINKn.
Updates

Target Market(s)

general public and trade

Industry/Entity Type

Auto Repair

Font styles to use
Serif
Sans Serif

Colors

Designer to choose colors to be used in the design.

Requirements
Must have
• copy description from my website
• coindrop link. to my site shop
• plenty of logo within reason
Nice to have
• scolling shop
• easy to manage

```html
<!DOCTYPE html>
<html lang="en">
<head>
<meta charset="utf-8">
<title>Brightpanel Bodyshop</title>
<link href="https://fonts.googleapis.com/css2?family=Montserrat:wght@300;400;500;600;700&display=swap" rel="stylesheet">
<style>
  :root {
    --bg: #000000;
    --white: #ffffff;
    --soft-white: #e6e6e6;
    --red: #ff1010;
    --car-light: #3a3a3c;
    --car-mid: #1a1a1b;
  }
  * { margin: 0; padding: 0; box-sizing: border-box; }
  html, body {
    width: 1200px; height: 581px; overflow: hidden;
    background: var(--bg);
  }
  .banner {
    position: relative;
    width: 1200px; height: 581px;
    background: var(--bg);
    font-family: "Montserrat", sans-serif;
    color: var(--white);
    overflow: hidden;
  }
  .car-photo {
    position: absolute;
    left: 0; top: 158px;
    width: 722px; height: 316px;
    background: radial-gradient(ellipse 60% 55% at 45% 50%, var(--car-light) 0%, var(--car-mid) 55%, var(--bg) 100%);
    border-radius: 40% 45% 12% 8% / 55% 55% 18% 18%;
  }
  .brand {
    position: absolute;
    left: 700px; top: 94px;
    width: 420px;
    text-align: right;
  }
  .brand-name {
    font-size: 42px;
    font-weight: 600;
    letter-spacing: 1px;
    color: var(--soft-white);
    line-height: 1;
  }
  .brand-tag {
    margin-top: 14px;
    margin-right: 74px;
    font-size: 18px;
    font-weight: 500;
    letter-spacing: 11px;
    color: var(--soft-white);
  }
  .headline {
    position: absolute;
    right: 86px; top: 222px;
    text-align: right;
    font-size: 29px;
    line-height: 36px;
    letter-spacing: 2px;
  }
  .headline-top { font-weight: 400; }
  .headline-accent { font-weight: 700; color: var(--red); letter-spacing: 0.5px; }
  .intro {
    position: absolute;
    right: 88px; top: 312px;
    width: 300px;
    text-align: right;
    font-size: 12.8px;
    font-weight: 300;
    line-height: 22.5px;
    letter-spacing: 0.5px;
  }
  .cta {
    position: absolute;
    left: 823px; top: 418px;
    width: 295px; height: 53px;
    background: var(--red);
    color: var(--white);
    font-size: 18px;
    font-weight: 600;
    letter-spacing: 0.5px;
    display: flex; align-items: center; justify-content: center;
    text-decoration: none;
  }
  .contacts {
    position: absolute;
    top: 526px; left: 226px;
    display: flex; gap: 106px;
    font-size: 15px;
    font-weight: 400;
    letter-spacing: 0.6px;
  }
  .contact { display: flex; align-items: center; gap: 8px; }
  .contact svg { display: block; }
</style>
</head>
<body>
<main class="banner">
  <div class="car-photo" role="img" aria-label="Photo of a black luxury coupé lit from the side on a black background"></div>

  <div class="brand">
    <div class="brand-name">BRIGHTPANEL</div>
    <div class="brand-tag">BODYSHOP</div>
  </div>

  <h1 class="headline">
    <span class="headline-top">YOUR ONE STOP</span><br>
    <span class="headline-accent">BODYSHOP</span>
  </h1>

  <p class="intro">From the repair of the smallest dents and scratches to major auto repair work, Brightpanel is set up to meet</p>

  <a class="cta" href="#">GET STARTED</a>

  <div class="contacts">
    <div class="contact">
      <svg width="16" height="16" viewBox="0 0 16 16" aria-hidden="true">
        <g fill="none" stroke="var(--red)" stroke-width="1.4">
          <circle cx="8" cy="8" r="7"/>
          <ellipse cx="8" cy="8" rx="3" ry="7"/>
          <line x1="1" y1="8" x2="15" y2="8"/>
          <line x1="2.2" y1="4.5" x2="13.8" y2="4.5"/>
          <line x1="2.2" y1="11.5" x2="13.8" y2="11.5"/>
        </g>
      </svg>
      <span>www.brightpanel.co.uk</span>
    </div>
    <div class="contact">
      <svg width="18" height="13" viewBox="0 0 18 13" aria-hidden="true">
        <rect x="0" y="0" width="18" height="13" fill="var(--red)"/>
        <polyline points="0.5,0.8 9,7.5 17.5,0.8" fill="none" stroke="var(--bg)" stroke-width="1.3"/>
        <line x1="0.5" y1="12.3" x2="6.5" y2="5.8" stroke="var(--bg)" stroke-width="1"/>
        <line x1="17.5" y1="12.3" x2="11.5" y2="5.8" stroke="var(--bg)" stroke-width="1"/>
      </svg>
      <span>sales@brightpanel.co.uk</span>
    </div>
  </div>
</main>
</body>
</html>
```